SkyRavelin Unique Gift Certificate

We need a unique, luxury gift certificate created for our online company (SkyRavelin). We are looking for something out of the ordinary, ie. do not want it to look like a 'normal' gift certificate. Please visit our website to gain a feel for our company (skyravelin.com.au). The dimensions are 148x148mm. We need our logo, website details, to, from, description, code, exp date included. The certificate will be printed on wood veneer so watermarks will not work. We want it to be clean and minimalistic.

Industry/Entity Type

It Company

```html
<!DOCTYPE html>
<html lang="en">
<head>
<meta charset="utf-8">
<title>SkyRavelin Gift Certificate</title>
<link rel="stylesheet" href="https://fonts.googleapis.com/css2?family=PT+Sans:wght@400;700&display=swap">
<style>
  :root {
    --page: #ffffff;
    --wood-light: #e2b887;
    --wood-mid: #d6a56f;
    --wood-dark: #c99560;
    --groove: #4a3526;
    --teal: #2f7f98;
    --cocoa: #3f2f29;
    --espresso: #2b221f;
    --stone: #d9d2cc;
    --mist: #e6e8ea;
    --ink-light: #f4eee8;
    --ink-dark: #2e2824;
    --font-body: "PT Sans", "Trebuchet MS", sans-serif;
  }
  html, body {
    margin: 0;
    padding: 0;
    width: 1200px;
    height: 927px;
    overflow: hidden;
    background: var(--page);
    font-family: var(--font-body);
  }
  .certificate {
    position: absolute;
    left: 127.5px;
    top: 229.5px;
    width: 630px;
    height: 613.5px;
    overflow: hidden;
  }
  .wood-veneer {
    position: absolute;
    inset: 0;
    background:
      repeating-linear-gradient(178deg, rgba(160,110,60,0.10) 0 2px, transparent 2px 7px),
      linear-gradient(180deg, var(--wood-light), var(--wood-mid) 55%, var(--wood-dark));
  }
  .hex-grid {
    position: absolute;
    inset: 0;
    width: 630px;
    height: 613.5px;
  }
  .hex { stroke: var(--groove); stroke-width: 1.3; stroke-linejoin: round; }
  .hex--wood { fill: rgba(255,240,220,0.08); }
  .hex--teal { fill: var(--teal); }
  .hex--cocoa { fill: var(--cocoa); }
  .hex--espresso { fill: var(--espresso); }
  .hex--stone { fill: var(--stone); }
  .hex--mist { fill: var(--mist); }
  .brand-ring { fill: none; stroke: var(--teal); stroke-width: 2.4; }

  .label {
    position: absolute;
    margin: 0;
    font-size: 16.5px;
    line-height: 1.3;
  }
  .label--light { color: var(--ink-light); }
  .label--dark { color: var(--ink-dark); }

  .description {
    position: absolute;
    left: 380px;
    top: 278px;
    width: 240px;
    margin: 0;
    text-align: center;
    font-size: 15.5px;
    line-height: 19px;
    letter-spacing: 1.1px;
    color: var(--ink-light);
  }
  .recipient { left: 180px; top: 492px; line-height: 25px; }
  .redeem { left: 415px; top: 622px; }
  .website { left: 180px; top: 767px; font-size: 16px; letter-spacing: 0.6px; }
  .brand-name {
    position: absolute;
    left: 640px;
    top: 802px;
    width: 140px;
    margin: 0;
    text-align: center;
    font-size: 15px;
    font-weight: 400;
    color: var(--ink-dark);
  }
</style>
</head>
<body>
  <main class="certificate">
    <div class="wood-veneer" role="img" aria-label="Light oak wood veneer grain"></div>
    <svg class="hex-grid" viewBox="85 153 420 409" preserveAspectRatio="none" aria-hidden="true">
      <polygon class="hex hex--wood" points="-61,77 -18,1 72,1 115,77 72,153 -18,153"/>
      <polygon class="hex hex--wood" points="-61,254 -18,178 72,178 115,254 72,330 -18,330"/>
      <polygon class="hex hex--wood" points="-61,431 -18,355 72,355 115,431 72,507 -18,507"/>
      <polygon class="hex hex--wood" points="-61,608 -18,532 72,532 115,608 72,684 -18,684"/>
      <polygon class="hex hex--wood" points="92,164 135,88 225,88 268,164 225,240 135,240"/>
      <polygon class="hex hex--teal" points="92,341 135,265 225,265 268,341 225,417 135,417"/>
      <polygon class="hex hex--espresso" points="92,518 135,442 225,442 268,518 225,594 135,594"/>
      <polygon class="hex hex--wood" points="245,77 288,-1 378,-1 421,77 378,153 288,153"/>
      <polygon class="hex hex--cocoa" points="245,254 288,178 378,178 421,254 378,330 288,330"/>
      <polygon class="hex hex--stone" points="245,431 288,355 378,355 421,431 378,507 288,507"/>
      <polygon class="hex hex--wood" points="245,608 288,532 378,532 421,608 378,684 288,684"/>
      <polygon class="hex hex--wood" points="398,164 441,88 531,88 574,164 531,240 441,240"/>
      <polygon class="hex hex--wood" points="398,341 441,265 531,265 574,341 531,417 441,417"/>
      <polygon class="hex hex--mist" points="398,518 441,442 531,442 574,518 531,594 441,594"/>
      <circle class="brand-ring" cx="473" cy="510" r="24"/>
    </svg>
  </main>

  <p class="description">here you can<br>write your gift<br>card description.<br>here you can write your<br>gift card description here<br>you can write your gift card<br>description here you can<br>write your gift card<br>description here you<br>can write your gift<br>card descrip-</p>

  <p class="label label--light recipient">to:<br>from:</p>
  <p class="label label--dark redeem">code:<br>expiration date:</p>
  <p class="label label--light website">www.skyravelin.com.au</p>
  <p class="brand-name">SkyRavelin</p>
</body>
</html>
```